Brisk Motion Flyer - Physiotherapy company

I am looking for a two-sided flyer (4"x8") that can be easily posted on cork boards or displayed as needed to provide information about my business. I would like to use the colors found in my logo (see attached) along with white and black. Please have a look at my website for ideas of how I would like the color schemes etc (www.briskmotion.example). I would like it to follow the same style as my website.<br/><br/>FRONT SIDE<br/>I am hoping to have the name of our business "Brisk Motion" with our slogan "Boreal Physiotherapy - Rehab and Recovery Above the Line (degrees symbol)" underneath. Somewhere above or around this I would like my logo (see attached). <br/><br/>Below that I would like a title "Services Provided" and then listed: <br/>Mobile Services<br/>Clinic<br/>Telehealth<br/><br/>Below that, I would like another title "Treatments Offered" and then listed: <br/>Hands-on manual therapy<br/>Intramuscular Stimulation (IMS)<br/>Acupuncture<br/>Athletic taping<br/>Injury/condition education<br/>Supervised exercise<br/><br/>Below that I would like "Contact Us":<br/>Brisk Motion<br/>www.BriskMotion.example<br/>Book online through https://briskmotion.bookerly.example/<br/>physio@briskmotion.example<br/>867-555-0148<br/>Direct Billing offered for most extended health providers<br/>(friendwall, Pictagram logo, movetrak logo (see attached) on bottom maybe in corner or centered)<br/><br/>BACK SIDE<br/><br/>I would like the logo on there once again maybe. Then I would like these three information sections one on top of the other spaced out appropriately.<br/><br/>Image (needling image) (see attached)<br/>Title: Mobile Physiotherapy<br/>The information below title: If you want to keep moving and need some help, but your current condition makes it difficult or unsafe to travel to and from a clinic to see a physiotherapist, that’s where we come in. We make it easy by offering a mobile service that provides exceptional one-on-one physiotherapy assessment and treatment in the comfort of your own home. There is a small fee to access mobile services. <br/><br/>Image (Hands on knee image) (see attached)<br/>Title: Clinic<br/>The information below title: If you have an injury that is causing you pain or restricting you from doing the activities that you want to do then physiotherapy can help. A traditional approach to physiotherapy where you come to our clinic and we provide one to one education and hands on therapy. <br/><br/>Image (computer, tablet etc) (see attached)<br/>Title: Telehealth<br/>The information below title: If you live outside of Whitehorse or just want easy access to a physiotherapist from the comfort of your home, then Telehealth is for you. Telehealth involves meeting with your physiotherapist using real-time technology, similar to ViewTalk. Brisk Motion utilizes Movetrakker for exercise prescription, pain tracking and telehealth. Through Movetrakker or it’s Kinetapp you can discuss your treatment plan, diagnoses, exercises, daily activities or any other questions you may have directly with a physiotherapist.<br/><br/><br/><br/>

Industry/Entity Type

Healthcare

Colors

Designer to choose colors to be used in the design.

Requirements
Must have
• Follow the same colors and schemes of my website (www.briskmotion.example)
• Keep it clean and concise
Nice to have
• Images might not fit because I don't want it too cluttered.
Should not have
• Too busy

```html
<!DOCTYPE html>
<html lang="en">
<head>
<meta charset="utf-8">
<title>Brisk Motion – Boreal Physiotherapy Flyer</title>
<link rel="stylesheet" href="https://fonts.googleapis.com/css2?family=Roboto+Slab:wght@300;400;700;800&family=Roboto:wght@400;500&display=swap">
<style>
  :root {
    --navy: #2a4571;
    --navy-deep: #1b2d55;
    --green: #0f5446;
    --green-deep: #073a30;
    --silver: #c4c6c9;
    --silver-dark: #8e9094;
    --white: #ffffff;
    --ink: #1d1d1f;
  }
  * { margin: 0; padding: 0; box-sizing: border-box; }
  html, body { width: 1200px; height: 2400px; overflow: hidden; background: var(--white); }
  .flyer { position: relative; width: 1200px; height: 2400px; overflow: hidden; font-family: "Roboto Slab", Georgia, serif; color: var(--ink); }
  .backdrop { position: absolute; inset: 0; }
  .hands-photo { position: absolute; left: 0; top: 1040px; width: 1200px; height: 960px;
    background: radial-gradient(ellipse at 65% 45%, #d9d9da 0%, #ececec 40%, rgba(255,255,255,0) 75%); }

  .brand-mark { position: absolute; top: 150px; left: 540px; width: 120px; height: 120px; border-radius: 50%; background: var(--navy); }
  .brand-name { position: absolute; top: 300px; left: 0; width: 1200px; text-align: center; color: var(--green); font-weight: 800; line-height: 1; }
  .brand-name .line-1 { display: block; font-size: 108px; letter-spacing: 10px; }
  .brand-name .line-2 { display: block; font-size: 52px; letter-spacing: 30px; margin-top: 28px; padding-left: 30px; }

  .hero { position: absolute; left: 0; width: 1200px; text-align: center; }
  .hero-name { top: 655px; color: var(--white); font-size: 72px; font-weight: 700; display: flex; justify-content: center; align-items: center; gap: 28px; }
  .hero-name::before, .hero-name::after { content: ""; width: 188px; height: 5px; background: var(--white); }
  .hero-title { top: 760px; font-size: 100px; font-weight: 700; color: #d0d1d3;
    background: linear-gradient(180deg, #ffffff 0%, #b9bbbe 60%, #e6e7e8 100%); -webkit-background-clip: text; background-clip: text; -webkit-text-fill-color: transparent;
    filter: drop-shadow(2px 3px 2px rgba(0,0,0,.35)); }
  .hero-tagline { top: 888px; font-family: "Roboto", Arial, sans-serif; font-size: 54px; color: var(--white); }

  .section-tab { position: absolute; left: 96px; height: 78px; background: var(--navy); color: var(--white); font-weight: 700; font-size: 44px; line-height: 80px; padding-left: 26px;
    clip-path: polygon(0 0, calc(100% - 46px) 0, 100% 100%, 0 100%); }
  .tab-services { top: 1180px; width: 566px; }
  .tab-treatments { top: 1517px; width: 630px; }

  .service { position: absolute; top: 1290px; text-align: center; font-size: 36px; font-weight: 300; color: var(--ink); }
  .service svg { display: block; margin: 0 auto 22px; }
  .service-mobile { left: 100px; width: 175px; }
  .service-clinic { left: 350px; width: 340px; }
  .service-tele { left: 750px; width: 265px; }
  .divider { position: absolute; top: 1290px; width: 2px; height: 200px; background: #d5d5d5; }

  .treatments { position: absolute; top: 1622px; left: 106px; list-style: none; font-size: 38px; font-weight: 400; line-height: 54px; }
  .treatments li::before { content: ""; display: inline-block; width: 17px; height: 17px; border-radius: 50%; background: var(--green); margin-right: 14px; vertical-align: 5px; }

  .billing-badge { position: absolute; left: 706px; top: 1776px; width: 344px; height: 344px; border-radius: 50%;
    background: linear-gradient(160deg, #e9eaeb, #9fa1a5); padding: 11px; }
  .billing-badge p { width: 100%; height: 100%; border-radius: 50%; background: var(--navy); color: var(--white); font-weight: 700; font-size: 34px; line-height: 42px;
    display: flex; align-items: center; justify-content: center; text-align: center; padding: 0 20px; }

  .contact { position: absolute; left: 112px; top: 2055px; color: var(--white); }
  .contact .label { font-size: 36px; font-weight: 700; line-height: 48px; }
  .contact .line { font-size: 36px; line-height: 48px; display: flex; align-items: center; gap: 12px; }
  .contact .strong { font-weight: 700; }
  .contact .gap { margin-left: 14px; }

  .partners { position: absolute; right: 62px; bottom: 48px; text-align: right; color: #d6d8da; font-family: "Roboto", Arial, sans-serif; }
  .partners .social { font-size: 28px; font-weight: 500; margin-bottom: 14px; }
  .partners .app { font-size: 52px; font-weight: 500; }
</style>
</head>
<body>
<div class="flyer">
  <svg class="backdrop" width="1200" height="2400" viewBox="0 0 1200 2400">
    <defs>
      <linearGradient id="silverSweep" x1="0" x2="1" y1="0" y2="0">
        <stop offset="0" stop-color="#9a9ca0"/><stop offset=".5" stop-color="#e8e9ea"/><stop offset="1" stop-color="#a8aaad"/>
      </linearGradient>
      <radialGradient id="navyBand" cx=".5" cy=".55" r=".7">
        <stop offset="0" stop-color="#2f5283"/><stop offset="1" stop-color="#1b2d55"/>
      </radialGradient>
      <radialGradient id="greenBase" cx=".3" cy=".3" r=".9">
        <stop offset="0" stop-color="#13614f"/><stop offset="1" stop-color="#06362c"/>
      </radialGradient>
    </defs>
    <path d="M0,495 Q700,560 1200,410 L1200,1380 Q900,1030 0,1030 Z" fill="url(#navyBand)"/>
    <path d="M0,552 Q700,520 1200,418 Q700,565 0,608 Z" fill="url(#silverSweep)"/>
    <path d="M0,1030 Q900,1030 1200,1380 L1200,1460 Q950,1060 0,1030 Z" fill="url(#silverSweep)"/>
    <path d="M0,2018 Q620,1880 1200,1975 L1200,2025 Q620,1920 0,2062 Z" fill="url(#silverSweep)"/>
    <path d="M0,2060 Q620,1918 1200,2022 L1200,2400 L0,2400 Z" fill="url(#greenBase)"/>
  </svg>

  <div class="hands-photo" role="img" aria-label="Faint photo of a physiotherapist's hands treating a knee"></div>
  <svg class="backdrop" width="1200" height="2400" viewBox="0 0 1200 2400" aria-hidden="true">
    <path d="M0,1030 Q900,1030 1200,1380 L1200,1460 Q950,1060 0,1030 Z" fill="url(#silverSweep)"/>
    <path d="M0,2018 Q620,1880 1200,1975 L1200,2025 Q620,1920 0,2062 Z" fill="url(#silverSweep)"/>
    <path d="M0,2060 Q620,1918 1200,2022 L1200,2400 L0,2400 Z" fill="url(#greenBase)"/>
    <path d="M1200,1380 Q900,1030 300,1031 L1200,1031 Z" fill="#1c2f58"/>
  </svg>

  <div class="brand-mark" aria-hidden="true"></div>
  <h1 class="brand-name"><span class="line-1">BRISK</span><span class="line-2">MOTION</span></h1>

  <p class="hero hero-name">Brisk Motion</p>
  <h2 class="hero hero-title">Boreal Physiotherapy</h2>
  <p class="hero hero-tagline">Rehab and Recovery Above the Line°</p>

  <h3 class="section-tab tab-services">SERVICES PROVIDED</h3>

  <div class="service service-mobile">
    <svg width="164" height="122" viewBox="0 0 164 122" fill="#0f5446">
      <rect x="90" y="0" width="30" height="14" rx="4"/>
      <path d="M12,28 H110 Q124,28 132,42 L150,66 Q164,70 164,84 V98 Q164,106 156,106 H12 Q2,106 2,96 V38 Q2,28 12,28 Z"/>
      <path d="M98,40 H118 L136,66 H98 Z" fill="#fff"/>
      <path d="M40,42 H52 V54 H64 V66 H52 V78 H40 V66 H28 V54 H40 Z" fill="#fff"/>
      <rect x="2" y="84" width="162" height="6" fill="#fff"/>
      <circle cx="36" cy="106" r="16" fill="#fff"/><circle cx="36" cy="106" r="11"/>
      <circle cx="126" cy="106" r="16" fill="#fff"/><circle cx="126" cy="106" r="11"/>
    </svg>
    MOBILE
  </div>
  <div class="divider" style="left:320px"></div>
  <div class="service service-clinic">
    <svg width="120" height="122" viewBox="0 0 120 122" fill="#0f5446">
      <rect x="14" y="0" width="92" height="26" rx="5"/>
      <rect x="24" y="8" width="72" height="10" rx="2" fill="#fff"/>
      <rect x="0" y="30" width="120" height="92"/>
      <g fill="#fff">
        <rect x="10" y="46" width="10" height="12"/><rect x="32" y="46" width="10" height="12"/><rect x="78" y="46" width="10" height="12"/><rect x="100" y="46" width="10" height="12"/>
        <rect x="10" y="76" width="10" height="12"/><rect x="100" y="76" width="10" height="12"/>
        <rect x="36" y="72" width="48" height="36"/>
      </g>
      <rect x="44" y="80" width="32" height="42"/>
    </svg>
    SERVICES CLINIC
  </div>
  <div class="divider" style="left:718px"></div>
  <div class="service service-tele">
    <svg width="188" height="122" viewBox="0 0 188 122" fill="#0f5446">
      <rect x="24" y="0" width="136" height="96" rx="6"/>
      <rect x="34" y="10" width="116" height="76" fill="#fff"/>
      <rect x="0" y="98" width="188" height="10" rx="4"/>
      <rect x="82" y="26" width="76" height="96" rx="6" stroke="#fff" stroke-width="5"/>
      <rect x="90" y="36" width="60" height="74" fill="#fff"/>
      <rect x="58" y="56" width="40" height="66" rx="5" stroke="#fff" stroke-width="5"/>
      <rect x="64" y="64" width="28" height="44" fill="#fff"/>
    </svg>
    TELEHEALTH
  </div>

  <h3 class="section-tab tab-treatments">TREATMENTS OFFERED</h3>
  <ul class="treatments">
    <li>Hands-on manual therapy</li>
    <li>Intramuscular Stimulation (IMS) Acupuncture</li>
    <li>Athletic taping</li>
    <li>Injury/condition education</li>
    <li>Supervised exercise</li>
  </ul>

  <div class="billing-badge"><p>Direct Billing offered for most extended health providers</p></div>

  <div class="contact">
    <p class="label">CONTACT US:</p>
    <p class="line">Brisk Motion</p>
    <p class="line strong" style="font-size:33px">
      <svg width="30" height="30" viewBox="0 0 30 30" fill="none" stroke="#fff" stroke-width="2.5"><circle cx="15" cy="15" r="12"/><ellipse cx="15" cy="15" rx="5" ry="12"/><path d="M3,15 H27"/></svg>
      www.BriskMotion.example
      <svg class="gap" width="34" height="28" viewBox="0 0 34 28" fill="#fff"><path d="M2,10 Q17,-2 32,10 L28,14 L24,10 V8 H10 V10 L6,14 Z"/><rect x="6" y="14" width="22" height="12" rx="2"/></svg>
      867-555-0148
    </p>
    <p class="label" style="margin-top:6px">Book online through</p>
    <p class="line" style="font-size:34px">
      <svg width="30" height="30" viewBox="0 0 30 30" fill="none" stroke="#fff" stroke-width="2.5"><circle cx="15" cy="15" r="12"/><ellipse cx="15" cy="15" rx="5" ry="12"/><path d="M3,15 H27"/></svg>
      https://briskmotion.bookerly.example
    </p>
    <p class="line" style="font-size:34px">
      <svg width="30" height="26" viewBox="0 0 30 26" fill="none" stroke="#fff" stroke-width="2.5"><rect x="2" y="4" width="26" height="19"/><path d="M2,4 L15,15 L28,4"/></svg>
      physio@briskmotion.example
    </p>
  </div>

  <div class="partners">
    <p class="social">Pictagram · Friendwall</p>
    <p class="app">Kinetapp</p>
  </div>
</div>
</body>
</html>
```